Criação de Papelaria (6 itens) para Beleza
" REALIZANDO CIRURGIAS PLÁSTICAS EM PACIENTES QUE DESEJAM MELHORIAS NO CONTORNO CORPORAL OU EM ALGO QUE OS INCOMODE EM SUA APARÊNCIA "

```html
<!DOCTYPE html>
<html lang="pt-BR">
<head>
<meta charset="UTF-8">
<title>Pasta — Lucas Verano Cirurgia Plástica</title>
<link href="https://fonts.googleapis.com/css2?family=Raleway:wght@300;400;500&display=swap" rel="stylesheet">
<style>
  :root{
    --backdrop:#e6e4e2;
    --paper:#ffffff;
    --paper-shade:#f1f1f1;
    --ink:#3a322f;
    --ink-soft:#6d6562;
    --rule:#4a403c;
    --decor:#e9e9ea;
  }
  *{box-sizing:border-box;margin:0;padding:0}
  html,body{width:1200px;height:1200px;overflow:hidden}
  body{background:var(--backdrop);font-family:"Raleway",sans-serif;color:var(--ink);position:relative}

  .folder-spread{position:absolute;left:80px;top:230px;width:1040px;height:740px;display:flex;
    box-shadow:0 10px 30px rgba(0,0,0,.12)}
  .folder-panel{position:relative;width:520px;height:740px;background:var(--paper);overflow:hidden}
  .folder-back{background:linear-gradient(120deg,var(--paper-shade),var(--paper) 60%)}
  .folder-front{border-left:1px solid #dcdcdc}

  /* back cover */
  .back-header{position:absolute;top:44px;left:30px;right:30px;height:20px;display:flex;align-items:center;gap:14px}
  .back-header .rule{flex:1;height:1px;background:var(--rule)}
  .back-brand{display:flex;align-items:center;gap:6px;white-space:nowrap}
  .brand-dot{border-radius:50%;background:var(--ink)}
  .back-brand .brand-dot{width:8px;height:8px}
  .back-brand .brand-name{font-size:11px;letter-spacing:1.5px;text-transform:uppercase;font-weight:400}
  .back-brand .brand-sub{font-size:6px;letter-spacing:2px;text-transform:uppercase;color:var(--ink-soft);display:block}

  .back-footer{position:absolute;left:30px;right:30px;bottom:34px}
  .back-footer .rule{height:1px;background:var(--rule)}
  .contact-row{display:flex;justify-content:space-between;align-items:center;padding:12px 4px}
  .contact-item{display:flex;align-items:center;gap:6px;font-size:8px;line-height:1.35;color:var(--ink-soft)}
  .contact-icon{width:14px;height:14px;flex:none}

  /* front cover */
  .front-top-rule{position:absolute;top:40px;left:0;right:0;height:1px;background:var(--rule)}
  .front-decor{position:absolute;left:40px;top:90px;width:250px;height:420px;
    background:radial-gradient(ellipse at 50% 45%,var(--decor),rgba(233,233,234,0) 70%)}
  .front-brand{position:absolute;left:190px;top:300px;display:flex;align-items:center;gap:14px}
  .front-brand .brand-dot{width:26px;height:26px}
  .front-brand .brand-name{font-size:27px;letter-spacing:1px;text-transform:uppercase;font-weight:400;line-height:1}
  .front-brand .brand-sub{font-size:10.5px;letter-spacing:5.2px;text-transform:uppercase;color:var(--ink-soft);margin-top:6px;font-weight:400}
  .pocket-slit{position:absolute;right:0;top:150px;width:40px;height:280px}
  .front-bottom-rules{position:absolute;left:0;right:0;bottom:98px}
  .front-bottom-rules .thick{height:3px;background:var(--rule)}
  .front-bottom-rules .thin{height:1px;background:var(--rule);margin-top:5px;opacity:.7}
</style>
</head>
<body>
  <main class="folder-spread">
    <section class="folder-panel folder-back">
      <header class="back-header">
        <span class="rule"></span>
        <div class="back-brand">
          <span class="brand-dot"></span>
          <div>
            <span class="brand-name">Lucas Verano</span>
            <span class="brand-sub">Cirurgia Plástica</span>
          </div>
        </div>
        <span class="rule"></span>
      </header>

      <footer class="back-footer">
        <div class="rule"></div>
        <div class="contact-row">
          <div class="contact-item">
            <svg class="contact-icon" viewBox="0 0 14 14"><circle cx="7" cy="7" r="6.5" fill="none" stroke="#6d6562"/><path d="M4.6 4.2l1.2-.4.8 1.6-.8.6c.4.9 1 1.5 1.9 1.9l.6-.8 1.6.8-.4 1.2c-2.6-.1-4.8-2.3-4.9-4.9z" fill="#6d6562"/></svg>
            <span>(00) 0000-0000<br>(00) 0000-0000</span>
          </div>
          <div class="contact-item">
            <svg class="contact-icon" viewBox="0 0 14 14"><circle cx="7" cy="7" r="6.5" fill="none" stroke="#6d6562"/><path d="M7 3.2a2.4 2.4 0 0 0-2.4 2.4C4.6 7.4 7 10.6 7 10.6s2.4-3.2 2.4-5A2.4 2.4 0 0 0 7 3.2zm0 3.3a.9.9 0 1 1 0-1.8.9.9 0 0 1 0 1.8z" fill="#6d6562"/></svg>
            <span>Rua Exemplo, 100<br>Cidade - Estado</span>
          </div>
          <div class="contact-item">
            <svg class="contact-icon" viewBox="0 0 14 14"><circle cx="7" cy="7" r="6.5" fill="none" stroke="#6d6562"/><rect x="3.8" y="4.8" width="6.4" height="4.4" fill="none" stroke="#6d6562" stroke-width=".8"/><path d="M3.8 4.8L7 7.3l3.2-2.5" fill="none" stroke="#6d6562" stroke-width=".8"/></svg>
            <span>contato@verano.med</span>
          </div>
          <div class="contact-item">
            <svg class="contact-icon" viewBox="0 0 14 14"><circle cx="7" cy="7" r="6.5" fill="none" stroke="#6d6562"/><circle cx="7" cy="7" r="2" fill="#6d6562"/></svg>
            <span>/verano.plastica</span>
          </div>
        </div>
        <div class="rule"></div>
      </footer>
    </section>

    <section class="folder-panel folder-front">
      <div class="front-top-rule"></div>
      <div class="front-decor" role="img" aria-label="Faint large brand symbol used as background decoration"></div>
      <div class="front-brand">
        <span class="brand-dot"></span>
        <div>
          <div class="brand-name">Lucas Verano</div>
          <div class="brand-sub">Cirurgia Plástica</div>
        </div>
      </div>
      <svg class="pocket-slit" viewBox="0 0 40 280" aria-hidden="true">
        <path d="M40 0 C 10 30, 10 60, 28 90 L 28 250 C 28 265, 34 275, 40 280" fill="none" stroke="#bdbdbd" stroke-width="1.2"/>
      </svg>
      <div class="front-bottom-rules">
        <div class="thick"></div>
        <div class="thin"></div>
      </div>
    </section>
  </main>
</body>
</html>
```